Vexo Systems Web Site Design

Need a basic site to show clients a little about what we do. We are a custom audio video company in the high-end residential market. Need a few basic but professional pages to show past projects and products we sell. No e-commerce. Should include my new logo from ArtHivePro.

Industry/Entity Type

Residential

Number of Pages Required

2 page

Font styles to use
Serif
Sans Serif

Colors
f78f20

Requirements
Must have
• Company Logo, Send feedback page
Nice to have
• I have no ideas about design, but I do know what I like and dislike when I see it.

```html
<!DOCTYPE html>
<html lang="en">
<head>
<meta charset="utf-8">
<title>Vexo Systems – High End Audio/Video</title>
<link href="https://fonts.googleapis.com/css2?family=Open+Sans:ital,wght@0,300;0,400;0,600;0,700;1,400&family=Open+Sans+Condensed:wght@300;700&display=swap" rel="stylesheet">
<style>
:root{
  --orange:#f78f20;
  --light:#eef2f8;
  --dark:#1d1d1d;
  --card-dark:#161616;
  --ink:#222;
  --muted:#666;
  --white:#fff;
  --line:#f6b77a;
}
*{margin:0;padding:0;box-sizing:border-box}
html,body{width:1200px;height:900px;overflow:hidden;background:var(--white)}
body{font-family:"Open Sans",Arial,sans-serif;color:var(--ink);position:relative}
.page{position:absolute;left:395px;top:0;width:418px;height:900px;background:var(--white)}
.abs{position:absolute}
.tiny{font-size:3.6px;line-height:5.4px}

/* header */
.site-header{left:0;top:0;width:418px;height:31px;background:var(--light)}
.brand{display:flex;align-items:center;gap:3px}
.brand-mark{width:9px;height:9px;background:var(--orange)}
.brand-name{font-size:5px;font-weight:700;color:var(--ink);line-height:5px;text-transform:uppercase;letter-spacing:.2px}
.site-header .brand{position:absolute;left:57px;top:10px}
.main-nav{position:absolute;left:222px;top:13px;display:flex;gap:7px;font-family:"Open Sans Condensed",Arial,sans-serif;font-weight:300;font-size:5.2px;color:var(--orange)}
.main-nav span{white-space:nowrap}
.main-nav .active{position:relative}
.main-nav .active::before{content:"";position:absolute;left:-2px;right:-2px;top:-13px;height:31px;background:rgba(255,255,255,.7);z-index:-1}
.main-nav .active::after{content:"";position:absolute;left:3px;right:3px;top:14px;height:4px;background:#888}

/* hero */
.hero{left:0;top:31px;width:418px;height:156px;background:linear-gradient(160deg,#2c2d33 0%,#4a4b53 40%,#35363d 70%,#202126 100%)}
.hero-title{left:0;top:79px;width:418px;text-align:center;color:var(--white);font-weight:300;font-size:16px;line-height:22px}
.hero-arrow{width:6px;height:10px}
.tiles{left:56px;top:138px;display:flex;gap:1px}
.tile{width:76px}
.tile-photo{height:49px;display:flex;align-items:center;justify-content:center;position:relative;color:var(--white);font-size:4px;font-weight:700;letter-spacing:.3px}
.tile-photo .badge{position:absolute;width:30px;height:30px;border-radius:50%;background:var(--orange);opacity:.85}
.tile-photo span{position:relative}
.tile-body{height:66px;background:var(--card-dark);color:#ddd;text-align:center;padding:16px 10px 0}
.tile-body svg{display:block;margin:0 auto 13px}

/* intro */
.intro-title{left:0;top:271px;width:418px;text-align:center;color:var(--orange);font-weight:700;font-size:17px;line-height:24px;letter-spacing:-.3px}
.intro-text{left:56px;top:297px;width:306px;text-align:center;color:var(--muted);font-size:3.6px;line-height:8px}
.tree{left:0;top:324px;width:418px;height:60px}
.feature{top:366px;width:92px;text-align:center}
.feature svg{display:block;margin:0 auto 8px}
.feature h3{font-size:4px;font-weight:700;margin-bottom:2px}
.feature p{color:var(--orange)}

/* projects */
.projects{left:0;top:438px;width:418px;height:125px;background:var(--light)}
.section-title{position:absolute;left:0;width:418px;text-align:center;color:var(--orange);font-weight:700;font-size:16px;line-height:22px;letter-spacing:-.3px}
.cards{position:absolute;left:56px;display:flex;gap:8px}
.card{width:97px;background:var(--white)}
.card .photo{height:51px}
.card p{padding:5px 7px;color:var(--muted);text-align:center;height:28px}
.nav-dot{position:absolute;width:9px;height:9px;border-radius:50%;background:#d4d7dc;display:flex;align-items:center;justify-content:center}

/* products */
.products{left:0;top:566px;width:418px;height:127px;background:var(--dark)}
.product{width:97px;height:81px;background:var(--white);position:relative}
.product .photo{position:absolute;left:4px;top:4px;right:4px;bottom:4px}
.product p{position:absolute;left:5px;right:5px;top:49px;height:24px;padding:3px;background:rgba(200,200,200,.9);color:#222;text-align:center}

/* testimonial */
.quote-title{left:0;top:716px;width:418px;text-align:center;font-weight:700;font-size:12px;line-height:17px;color:var(--ink);letter-spacing:-.2px}
.quote-text{left:86px;top:738px;width:246px;text-align:center;font-style:italic;color:var(--muted);font-size:3.9px;line-height:7px}
.quote-by{left:0;top:765px;width:418px;text-align:center;color:var(--orange);font-size:3.3px}
.dots{left:204px;top:781px;display:flex;gap:1.5px}
.dots i{width:2px;height:2px;border-radius:50%;background:#ccc}
.dots i:first-child{background:var(--orange)}

/* footer */
.footer-rule{left:56px;top:827px;width:306px;height:1px;background:#cfd6df}
.footer-badge{left:183px;top:801px;width:52px;height:52px;border-radius:50%;background:var(--light);display:flex;align-items:center;justify-content:center}
.footer-nav{top:834px;display:flex;gap:8px;font-family:"Open Sans Condensed",Arial,sans-serif;font-weight:300;font-size:5px;color:var(--ink)}
.contact-band{left:0;top:847px;width:418px;height:34px;background:var(--orange);color:var(--white);font-size:5px;font-weight:700}
.contact-band .call{position:absolute;left:83px;top:14px}
.contact-band .mail{position:absolute;left:290px;top:14px}
.social{position:absolute;left:185px;top:14px;display:flex;gap:5px}
.social i{width:5px;height:5px;border:1px solid var(--white)}
.legal{left:0;top:884px;width:418px;text-align:center;font-size:3.4px;color:var(--muted)}
.legal-rule{left:139px;top:893px;width:139px;height:1px;background:var(--line)}
</style>
</head>
<body>
<div class="page">

  <header class="site-header abs">
    <div class="brand"><span class="brand-mark"></span><span class="brand-name">Vexo<br>Systems</span></div>
    <nav class="main-nav">
      <span class="active">HOME</span><span>ABOUT</span><span>AUDIO/VIDEO</span><span>SERVICES</span><span>WORKS</span><span>CONTACT US</span>
    </nav>
  </header>

  <section class="hero abs" role="img" aria-label="Close-up photo of a dark loudspeaker grille">
    <h1 class="hero-title abs" style="top:48px">High End AUDIO/VIDEO Solutions</h1>
    <svg class="hero-arrow abs" style="left:52px;top:57px" viewBox="0 0 6 10"><path d="M5 1L1 5l4 4" fill="none" stroke="#f78f20" stroke-width="1.6"/></svg>
    <svg class="hero-arrow abs" style="left:360px;top:57px" viewBox="0 0 6 10"><path d="M1 1l4 4-4 4" fill="none" stroke="#f78f20" stroke-width="1.6"/></svg>
  </section>

  <div class="tiles abs">
    <div class="tile">
      <div class="tile-photo" role="img" aria-label="Photo of a modern home theater room" style="background:linear-gradient(180deg,#6d6e72,#3b3c40)"><i class="badge"></i><span>ABOUT US</span></div>
      <div class="tile-body tiny"><svg width="5" height="5" viewBox="0 0 5 5"><path d="M1 4L4 1M1.5 2.5L2.5 1.5" stroke="#f78f20" stroke-width="1" stroke-linecap="round"/></svg>Aliquam dapibus tincidunt metus. Praesent justo dolor, lobortis quis, lobortis...</div>
    </div>
    <div class="tile">
      <div class="tile-photo" role="img" aria-label="Photo of a mixing console" style="background:linear-gradient(180deg,#3a3a3d,#1a1a1b)"><span>SERVICES</span></div>
      <div class="tile-body tiny"><svg width="5" height="5" viewBox="0 0 5 5"><path d="M1 4L4 1M1.5 2.5L2.5 1.5" stroke="#f78f20" stroke-width="1" stroke-linecap="round"/></svg>Aliquam dapibus tincidunt metus. Praesent justo dolor, lobortis quis, lobortis...</div>
    </div>
    <div class="tile">
      <div class="tile-photo" role="img" aria-label="Photo of a speaker grille" style="background:#1c1c1d"><span>AUDIO</span></div>
      <div class="tile-body tiny"><svg width="5" height="5" viewBox="0 0 5 5"><path d="M1 4L4 1M1.5 2.5L2.5 1.5" stroke="#f78f20" stroke-width="1" stroke-linecap="round"/></svg>Aliquam dapibus tincidunt metus. Praesent justo dolor, lobortis quis, lobortis...</div>
    </div>
    <div class="tile">
      <div class="tile-photo" role="img" aria-label="Photo of a cinema room with a projection screen" style="background:linear-gradient(180deg,#8e8f93,#3e3f43)"><span>VIDEO</span></div>
      <div class="tile-body tiny"><svg width="5" height="5" viewBox="0 0 5 5"><path d="M1 4L4 1M1.5 2.5L2.5 1.5" stroke="#f78f20" stroke-width="1" stroke-linecap="round"/></svg>Aliquam dapibus tincidunt metus. Praesent justo dolor, lobortis quis, lobortis...</div>
    </div>
  </div>

  <h2 class="intro-title abs">Nothing is Impossible</h2>
  <p class="intro-text abs">Etiam maximus leo tristique purus posuere, sed malesuada eros efficitur. Morbi augue tellus, condimentum in tempor nec, lobortis non metus. Pellentesque at consectetur massa. Aliquam tellus mauris, rhoncus accumsan ultrices eu, semper vitae nunc. Cras malesuada mollis lorem, a auctor diam condimentum in. Suspendisse consequat vel est sed eleifend. Phasellus id risus at arcu vulputate commodo. Fusce vitae nulla in arcu luctus imperdiet et nec est.</p>

  <svg class="tree abs" viewBox="0 0 418 60">
    <path d="M209 1V28M95 28H323M95 28V36M209 28V36M323 28V36" fill="none" stroke="#f6b77a" stroke-width=".8"/>
  </svg>
  <div class="feature abs" style="left:49px">
    <svg width="12" height="12" viewBox="0 0 12 12"><path d="M7 0.5L2 7h3.5L4.5 11.5 10 5H6.5z" fill="#f78f20"/></svg>
    <h3>ELECTRIFY PEOPLE</h3><p class="tiny">Aenean et hendrerit erat, ac euismod nunc. Proin fringilla eros nec egestas. Cras pharetra ipsum ut sapien placerat malesuada.</p></div>
  <div class="feature abs" style="left:163px">
    <svg width="12" height="12" viewBox="0 0 12 12"><g fill="none" stroke="#f78f20" stroke-width="1.4" stroke-linecap="round"><path d="M2 10.5a0.1 0.1 0 0 1 0 0"/><path d="M2 7a3.5 3.5 0 0 1 3.5 3.5"/><path d="M2 4a6.5 6.5 0 0 1 6.5 6.5"/><path d="M2 1a9.5 9.5 0 0 1 9.5 9.5"/></g></svg>
    <h3>KEEP IT SIMPLE</h3><p class="tiny">Aenean et hendrerit erat, ac euismod nunc. Proin fringilla eros nec egestas. Cras pharetra ipsum ut sapien placerat malesuada.</p></div>
  <div class="feature abs" style="left:277px">
    <svg width="14" height="12" viewBox="0 0 14 12"><path d="M1 4.5h3L10 1v10L4 7.5H1z" fill="#f78f20"/><path d="M4 7.5l1 3.5h2L6 7.5" fill="#f78f20"/><path d="M11.5 4l2-1.2M11.5 6h2.2M11.5 8l2 1.2" stroke="#f78f20" stroke-width=".9"/></svg>
    <h3>SPREAD THE WORD</h3><p class="tiny">Aenean et hendrerit erat, ac euismod nunc. Proin fringilla eros nec egestas. Cras pharetra ipsum ut sapien placerat malesuada.</p></div>

  <section class="projects abs">
    <h2 class="section-title" style="top:6px">Our Projects</h2>
    <i class="nav-dot" style="left:37px;top:69px"><svg width="3" height="4" viewBox="0 0 3 4"><path d="M2.5 .5L.8 2l1.7 1.5" fill="none" stroke="#fff" stroke-width=".7"/></svg></i>
    <i class="nav-dot" style="left:372px;top:69px"><svg width="3" height="4" viewBox="0 0 3 4"><path d="M.5 .5L2.2 2 .5 3.5" fill="none" stroke="#fff" stroke-width=".7"/></svg></i>
    <div class="cards" style="top:36px">
      <div class="card"><div class="photo" role="img" aria-label="Photo of a home theater with red seating" style="background:linear-gradient(180deg,#3a3a3c 0%,#6e6e72 45%,#2a2a2c 70%,#8a1e1e 100%)"></div><p class="tiny">Lorem ipsum dolor sit amet, consectetur adipiscing elit. Sed blandit massa vel mauris sollicitudin dignissim. Phasellus ultrices tellus eget ipsum...</p></div>
      <div class="card"><div class="photo" role="img" aria-label="Photo of a living room with wall-mounted TV" style="background:linear-gradient(90deg,#e4e6ea 0%,#c9cbd0 40%,#d9822b 50%,#5a5a5e 62%,#2e2e31 100%)"></div><p class="tiny">Lorem ipsum dolor sit amet, consectetur adipiscing elit. Sed blandit massa vel mauris sollicitudin dignissim. Phasellus ultrices tellus eget ipsum...</p></div>
      <div class="card"><div class="photo" role="img" aria-label="Photo of audio mixer controls" style="background:linear-gradient(160deg,#4a4a4d,#1a1a1b)"></div><p class="tiny">Lorem ipsum dolor sit amet, consectetur adipiscing elit. Sed blandit massa vel mauris sollicitudin dignissim. Phasellus ultrices tellus eget ipsum...</p></div>
    </div>
  </section>

  <section class="products abs">
    <h2 class="section-title" style="top:6px">Products</h2>
    <i class="nav-dot" style="left:37px;top:70px;background:#444"><svg width="3" height="4" viewBox="0 0 3 4"><path d="M2.5 .5L.8 2l1.7 1.5" fill="none" stroke="#999" stroke-width=".7"/></svg></i>
    <i class="nav-dot" style="left:372px;top:70px;background:#444"><svg width="3" height="4" viewBox="0 0 3 4"><path d="M.5 .5L2.2 2 .5 3.5" fill="none" stroke="#999" stroke-width=".7"/></svg></i>
    <div class="cards" style="top:35px">
      <div class="product"><div class="photo" role="img" aria-label="Product photo of a camcorder" style="background:linear-gradient(180deg,#f4f4f4,#d6d6d8)"></div><p class="tiny">Lorem ipsum dolor sit amet, consectetur adipiscing elit. Cras efficitur, mi vitae posuere felis tempus sed, non dolor volutpat.</p></div>
      <div class="product"><div class="photo" role="img" aria-label="Product photo of a coiled video cable" style="background:linear-gradient(180deg,#f7f7f7,#e0e0e2)"></div><p class="tiny">Lorem ipsum dolor sit amet, consectetur adipiscing elit. Cras efficitur, mi vitae posuere felis tempus sed, non dolor volutpat.</p></div>
      <div class="product"><div class="photo" role="img" aria-label="Product photo of red and white headphones" style="background:linear-gradient(180deg,#fbeaea,#f1c9c9)"></div><p class="tiny">Lorem ipsum dolor sit amet, consectetur adipiscing elit. Cras efficitur, mi vitae posuere felis tempus sed, non dolor volutpat.</p></div>
    </div>
  </section>

  <h2 class="quote-title abs">HEAR YE! HEAR YE!</h2>
  <svg class="abs" style="left:56px;top:743px" width="5" height="8" viewBox="0 0 5 8"><path d="M4 1L1 4l3 3" fill="none" stroke="#f78f20" stroke-width="1.3"/></svg>
  <svg class="abs" style="left:358px;top:743px" width="5" height="8" viewBox="0 0 5 8"><path d="M1 1l3 3-3 3" fill="none" stroke="#f78f20" stroke-width="1.3"/></svg>
  <p class="quote-text abs">Nulla dui. Fusce feugiat malesuada odio. Morbi nunc odio gravida at cursus nec luctus a lorem. Maecenas tristique orci ac sem. Duis ultricies pharetra magna. Donec accumsan malesuada orci. Donec sit amet eros. Lorem ipsum dolor sit amet consectetur adipiscing elit.</p>
  <p class="quote-by abs">July 14, 2015 by Jane</p>
  <div class="dots abs"><i></i><i></i><i></i></div>

  <footer>
    <div class="footer-rule abs"></div>
    <div class="footer-badge abs"><div class="brand"><span class="brand-mark"></span><span class="brand-name">Vexo<br>Systems</span></div></div>
    <nav class="footer-nav abs" style="left:83px"><span>HOME</span><span>ABOUT</span><span>AUDIO /VIDEO</span></nav>
    <nav class="footer-nav abs" style="left:271px"><span>SERVICES</span><span>WORKS</span><span>CONTACT US</span></nav>
    <div class="contact-band abs">
      <span class="call">CALL US: 217-555-0148</span>
      <div class="social" aria-label="Social links"><i></i><i></i><i></i><i></i><i></i></div>
      <span class="mail">EMAIL: info@vexosys.com</span>
    </div>
    <p class="legal abs">© 2015 PRIVACY POLICY</p>
    <div class="legal-rule abs"></div>
  </footer>

</div>
</body>
</html>
```